business card design

i would like business cards designed. My business provides trade qualified personnel to the mining industry to work on heavy mobile equipment.
please put a excavator(digger) in the background in one design and have one design without so i can compare the difference.
also add info:
my logo(attached) and "mobile equipment repair and maintenance"
name: Derek Holloway
address: 57 Tarrowby RD Carmel Perth WA.
mobile: 0438120957
email: derek@ironvalemx.com

```html
<!DOCTYPE html>
<html lang="en">
<head>
<meta charset="utf-8">
<title>Ironvale Maintenance Services – Business Card</title>
<link rel="stylesheet" href="https://fonts.googleapis.com/css2?family=Questrial&display=swap">
<style>
  :root {
    --backdrop: #1795ab;
    --navy: #001d40;
    --band-blue: #0b3a78;
    --accent-blue: #1a7ef0;
    --paper: #ffffff;
    --art-grey: #c9c9c9;
  }
  * { margin: 0; padding: 0; box-sizing: border-box; }
  html, body {
    width: 960px;
    height: 1200px;
    overflow: hidden;
    background: var(--backdrop);
  }
  .canvas {
    position: relative;
    width: 960px;
    height: 1200px;
    font-family: "Questrial", "Century Gothic", sans-serif;
  }
  .card {
    position: absolute;
    left: 142px;
    width: 676px;
    height: 426px;
    overflow: hidden;
  }
  .card--front { top: 145px; background: var(--paper); }
  .card--back { top: 628px; background: var(--navy); }
  .card__swoosh {
    position: absolute;
    inset: 0;
    width: 100%;
    height: 100%;
  }
  .brand {
    position: absolute;
    top: 52px;
    left: 0;
    width: 100%;
    text-align: center;
    color: var(--navy);
  }
  .brand__name {
    font-size: 58px;
    letter-spacing: 5px;
    line-height: 1;
  }
  .brand__legal {
    margin-top: 8px;
    font-size: 15px;
    letter-spacing: 2px;
    color: var(--accent-blue);
  }
  .hero-art {
    position: absolute;
    left: 207px;
    top: 167px;
    width: 245px;
    height: 139px;
    background: linear-gradient(180deg, #d4d4d4, var(--art-grey));
    border-radius: 6px;
  }
  .tagline {
    position: absolute;
    left: 150px;
    top: 330px;
    width: 390px;
    text-align: center;
    font-size: 24px;
    line-height: 39px;
    color: var(--accent-blue);
  }
  .contact {
    position: absolute;
    left: 0;
    top: 135px;
    width: 645px;
    text-align: center;
    color: var(--paper);
    font-size: 24px;
    line-height: 38px;
  }
  .contact__name { font-size: 25px; margin-bottom: 5px; }
</style>
</head>
<body>
<main class="canvas">
  <section class="card card--front">
    <svg class="card__swoosh" viewBox="0 0 676 426" preserveAspectRatio="none" aria-hidden="true">
      <path d="M663,0 C630,200 585,355 504,426 L676,426 L676,0 Z" fill="var(--band-blue)"/>
      <path d="M676,0 C648,200 605,355 529,426 L676,426 Z" fill="var(--navy)"/>
    </svg>
    <div class="brand">
      <div class="brand__name">IRONVALE</div>
      <div class="brand__legal">MAINTENANCE SERVICES PTY LTD</div>
    </div>
    <div class="hero-art" role="img" aria-label="Grey silhouette of a tracked excavator standing on a ground line"></div>
    <p class="tagline">MOBILE EQUIPMENT REPAIR &amp; MAINTENANCE</p>
  </section>

  <section class="card card--back">
    <svg class="card__swoosh" viewBox="0 0 676 426" preserveAspectRatio="none" aria-hidden="true">
      <path d="M659,0 C625,200 590,355 520,426 L676,426 L676,0 Z" fill="var(--band-blue)"/>
      <path d="M676,0 C648,200 610,355 538,426 L676,426 Z" fill="var(--paper)"/>
    </svg>
    <div class="contact">
      <p class="contact__name">DEREK HOLLOWAY</p>
      <p class="contact__line">mobile: 0438120957</p>
      <p class="contact__line">Address: 57 Tarrowby RD Carmel Perth WA</p>
      <p class="contact__line">Email: derek@ironvalemx.com</p>
    </div>
  </section>
</main>
</body>
</html>
```